Car transport business

We need a new business card design. Attached is our old card sample. I would just like to adjust the logo colors (blue and red) to be brighter. I changed my name to the brighter red and the word dispatcher to a brighter blue as an example. But you can adjust those colors further. And then perhaps you can use the same colors for the card design but use your imagination.

As a suggestion so the card stands out I would like to add a clip art of car carrier truck. Attached are examples of that as well

```html
<!DOCTYPE html>
<html lang="en">
<head>
<meta charset="utf-8">
<title>Northway Haul — Business Card</title>
<link href="https://fonts.googleapis.com/css2?family=Fira+Sans:wght@400;500;700;800&display=swap" rel="stylesheet">
<style>
  :root {
    --blue: #1f63d2;
    --red: #e91e2b;
    --paper: #ffffff;
    --backdrop: #e4e4e4;
  }
  * { box-sizing: border-box; margin: 0; padding: 0; }
  html, body {
    width: 1200px; height: 750px; overflow: hidden;
    background: var(--backdrop);
    font-family: "Fira Sans", sans-serif;
  }
  .card {
    position: absolute; left: 420px; width: 442px; height: 252px;
    background: var(--paper); overflow: hidden;
  }
  .card--front { top: 75px; }
  .card--back { top: 397px; }
  .card__bands { position: absolute; inset: 0; width: 100%; height: 100%; }

  .brand { position: absolute; display: flex; align-items: center; }
  .brand__dot { border-radius: 50%; background: var(--red); flex: none; }
  .brand__text { display: flex; flex-direction: column; }
  .brand__name { color: var(--blue); font-weight: 800; letter-spacing: 0.02em; line-height: 1; }
  .brand__tagline { color: var(--blue); font-weight: 500; text-transform: uppercase; line-height: 1; }

  .card--front .brand { left: 84px; top: 112px; gap: 10px; }
  .card--front .brand__dot { width: 30px; height: 30px; }
  .card--front .brand__name { font-size: 28px; }
  .card--front .brand__tagline { font-size: 8.5px; letter-spacing: 0.28em; margin-top: 4px; }

  .card--back .brand { left: 316px; top: 24px; gap: 5px; }
  .card--back .brand__dot { width: 14px; height: 14px; }
  .card--back .brand__name { font-size: 12.5px; }
  .card--back .brand__tagline { font-size: 4.2px; letter-spacing: 0.2em; margin-top: 2px; }

  .person { position: absolute; left: 46px; top: 78px; }
  .person__name { color: var(--red); font-size: 19px; font-weight: 500; line-height: 1.1; }
  .person__role { color: var(--blue); font-size: 9.5px; font-weight: 500; letter-spacing: 0.3em; margin-top: 2px; }

  .contacts { position: absolute; left: 43px; top: 125px; list-style: none; }
  .contacts__item { display: flex; align-items: center; gap: 9px; color: var(--red); font-size: 12px; height: 18px; }
  .contacts__icon { width: 11px; height: 11px; flex: none; fill: var(--red); }
</style>
</head>
<body>

<section class="card card--front">
  <svg class="card__bands" viewBox="0 0 442 252" preserveAspectRatio="none" aria-hidden="true">
    <polygon fill="var(--blue)" points="0,200 442,178 442,252 0,252"/>
    <polygon fill="var(--red)" points="0,226 442,210 442,252 0,252"/>
  </svg>
  <div class="brand">
    <span class="brand__dot"></span>
    <div class="brand__text">
      <span class="brand__name">NORTHWAY HAUL</span>
      <span class="brand__tagline">Vehicle Shipping Specialists</span>
    </div>
  </div>
</section>

<section class="card card--back">
  <svg class="card__bands" viewBox="0 0 442 252" preserveAspectRatio="none" aria-hidden="true">
    <polygon fill="var(--blue)" points="0,185 442,205 442,252 0,252"/>
    <polygon fill="var(--red)" points="0,212 442,228 442,252 0,252"/>
  </svg>
  <div class="brand">
    <span class="brand__dot"></span>
    <div class="brand__text">
      <span class="brand__name">NORTHWAY HAUL</span>
      <span class="brand__tagline">Vehicle Shipping Specialists</span>
    </div>
  </div>
  <div class="person">
    <p class="person__name">Dana Merrow</p>
    <p class="person__role">DISPATCHER</p>
  </div>
  <ul class="contacts">
    <li class="contacts__item">
      <svg class="contacts__icon" viewBox="0 0 24 24" aria-hidden="true"><path d="M6.6 10.8a15.1 15.1 0 0 0 6.6 6.6l2.2-2.2c.3-.3.7-.4 1-.2 1.1.4 2.3.6 3.6.6.6 0 1 .4 1 1V20c0 .6-.4 1-1 1A17 17 0 0 1 3 4c0-.6.4-1 1-1h3.5c.6 0 1 .4 1 1 0 1.3.2 2.5.6 3.6.1.3 0 .7-.2 1z"/></svg>
      <span>555-310-4827</span>
    </li>
    <li class="contacts__item">
      <svg class="contacts__icon" viewBox="0 0 24 24" aria-hidden="true"><path d="M7 2h8v5H7zM3 8h18v13H3zm3 3v2h3v-2zm5 0v2h3v-2zm5 0v2h3v-2zM6 15v2h3v-2zm5 0v2h3v-2zm5 0v2h3v-2z"/></svg>
      <span>555-310-4890</span>
    </li>
    <li class="contacts__item">
      <svg class="contacts__icon" viewBox="0 0 24 24" aria-hidden="true"><path d="M2 5h20v14H2zm2 2v.5l8 5.5 8-5.5V7l-8 5z"/></svg>
      <span>northwayhaul@mail.com</span>
    </li>
  </ul>
</section>

</body>
</html>
```